Brightpath Strategic Advisers F.Z.E
Professional
Khalid Yousef Nasser
Founder & CEO
Corvana Trade Park
info@bsa-qx.com
www.bsa-qx.com
Training & Consultancy on:
QBXR Assessment & Training
Leadership Development & Coaching
Change Management
Strategy Management
Performance Management
Quality & Process Management
TQM
HR Development
HR Procedures & Regulation
Logo & Full Stationeries & P.P Presentation first page and continues sheet & Proposal document cover & continues sheet

```html
<!DOCTYPE html>
<html lang="en">
<head>
<meta charset="utf-8">
<title>Brightpath Strategic Advisers – Stationery</title>
<link href="https://fonts.googleapis.com/css2?family=Open+Sans:wght@400;600;700&display=swap" rel="stylesheet">
<style>
  :root {
    --orange: #f07c1e;
    --orange-light: #f7a441;
    --grey: #6d6e70;
    --grey-dark: #3c3d3f;
    --ink: #4a4a4a;
    --paper: #ffffff;
    --stage: #efeae4;
    --label: #8a8178;
  }
  * { box-sizing: border-box; margin: 0; padding: 0; }
  html, body { width: 1200px; height: 317px; overflow: hidden; }
  body { background: var(--stage); font-family: "Open Sans", Arial, sans-serif; color: var(--ink); position: relative; }
  .sheet { position: absolute; background: var(--paper); box-shadow: 0 1px 4px rgba(0,0,0,.25); overflow: hidden; }
  .sheet svg.swoosh { position: absolute; left: 0; width: 100%; }
  .label { position: absolute; font-size: 4px; color: var(--label); white-space: nowrap; }
  .brand { position: absolute; display: flex; align-items: center; gap: 3px; color: var(--orange); font-weight: 700; line-height: 1.1; }
  .brand .dot { border-radius: 50%; background: var(--orange); flex: none; }
  .brand span.name { text-transform: uppercase; }
  .brand.on-dark { color: var(--paper); }
  .brand.on-dark .dot { background: var(--paper); }
  .card { width: 92px; height: 53px; }
  .card.dark { background: var(--grey-dark); color: #ddd; }
  .card .person { position: absolute; left: 8px; top: 14px; font-size: 4.5px; font-weight: 700; color: var(--orange); }
  .card .role { position: absolute; left: 8px; top: 20px; font-size: 3.5px; }
  .card .contact { position: absolute; left: 8px; bottom: 6px; font-size: 3px; line-height: 1.4; }
  .footer-line { position: absolute; left: 12px; right: 12px; height: 1px; background: var(--orange); }
  .footer-text { position: absolute; left: 12px; right: 12px; font-size: 3.2px; color: var(--grey); text-align: center; }
  .envelope-flap { position: absolute; left: 0; right: 0; top: 0; height: 48%; clip-path: polygon(0 0,100% 0,100% 40%,50% 100%,0 40%); }
</style>
</head>
<body>

<!-- Business cards -->
<div class="sheet card" style="left:12px;top:150px;">
  <div class="brand" style="left:8px;top:5px;font-size:3.6px;"><i class="dot" style="width:5px;height:5px"></i><span class="name">Brightpath Strategic Advisers</span></div>
  <div class="person">Khalid Yousef Nasser</div>
  <div class="role">Founder &amp; CEO</div>
  <div class="contact">Corvana Trade Park<br>info@bsa-qx.com · www.bsa-qx.com</div>
</div>
<div class="sheet card dark" style="left:110px;top:150px;">
  <div class="brand on-dark" style="left:14px;top:20px;font-size:4.5px;"><i class="dot" style="width:8px;height:8px"></i><span class="name">Brightpath Strategic<br>Advisers F.Z.E</span></div>
</div>
<div class="label" style="left:12px;top:206px;">Business Card Front</div>
<div class="label" style="left:110px;top:206px;">Business Card Back</div>

<div class="sheet card dark" style="left:12px;top:216px;">
  <div class="brand" style="left:8px;top:5px;font-size:3.6px;"><i class="dot" style="width:5px;height:5px"></i><span class="name">Brightpath Strategic Advisers</span></div>
  <div class="person">Khalid Yousef Nasser</div>
  <div class="role">Founder &amp; CEO</div>
  <div class="contact">Corvana Trade Park<br>info@bsa-qx.com · www.bsa-qx.com</div>
</div>
<div class="sheet card dark" style="left:110px;top:216px;">
  <div class="brand" style="left:14px;top:20px;font-size:4.5px;"><i class="dot" style="width:8px;height:8px"></i><span class="name">Brightpath Strategic<br>Advisers F.Z.E</span></div>
</div>

<!-- Letterhead first page -->
<div class="sheet" style="left:228px;top:10px;width:180px;height:290px;">
  <div class="brand" style="left:12px;top:10px;font-size:4.5px;"><i class="dot" style="width:9px;height:9px"></i><span class="name">Brightpath Strategic<br>Advisers F.Z.E</span></div>
  <svg class="swoosh" style="top:0;height:40px" viewBox="0 0 180 40" preserveAspectRatio="none" aria-hidden="true">
    <path d="M90 0 H180 V22 C150 10 120 6 90 0Z" fill="var(--grey)"/>
    <path d="M110 0 H180 V12 C160 5 135 2 110 0Z" fill="var(--orange)"/>
  </svg>
  <svg class="swoosh" style="bottom:0;height:36px" viewBox="0 0 180 36" preserveAspectRatio="none" aria-hidden="true">
    <path d="M0 10 C50 30 120 30 180 14 V36 H0Z" fill="var(--grey)"/>
    <path d="M0 20 C60 36 130 34 180 24 V36 H0Z" fill="var(--orange)"/>
  </svg>
  <div class="footer-text" style="bottom:40px;">Corvana Trade Park · info@bsa-qx.com · www.bsa-qx.com</div>
</div>
<div class="label" style="left:290px;top:303px;">Letterhead First Page</div>

<!-- Continuation sheet -->
<div class="sheet" style="left:440px;top:10px;width:190px;height:290px;">
  <svg class="swoosh" style="top:0;height:30px" viewBox="0 0 190 30" preserveAspectRatio="none" aria-hidden="true">
    <path d="M0 0 H190 V10 C130 4 60 4 0 24Z" fill="var(--grey)"/>
    <path d="M60 0 H190 V5 C140 2 100 2 60 0Z" fill="var(--orange)"/>
  </svg>
  <div class="brand" style="left:12px;top:20px;font-size:4.5px;"><i class="dot" style="width:9px;height:9px"></i><span class="name">Brightpath Strategic<br>Advisers F.Z.E</span></div>
  <div class="footer-line" style="bottom:20px;"></div>
  <div class="footer-text" style="bottom:12px;">Corvana Trade Park · info@bsa-qx.com · www.bsa-qx.com</div>
</div>
<div class="label" style="left:510px;top:303px;">Continuation Sheet</div>

<!-- Compliment slip -->
<div class="sheet" style="left:660px;top:108px;width:156px;height:114px;">
  <svg class="swoosh" style="top:0;height:18px" viewBox="0 0 156 18" preserveAspectRatio="none" aria-hidden="true">
    <path d="M0 0 H156 V6 C100 2 50 4 0 14Z" fill="var(--grey)"/>
    <path d="M50 0 H156 V3 C120 1 80 1 50 0Z" fill="var(--orange)"/>
  </svg>
  <div class="brand" style="left:10px;top:16px;font-size:4px;"><i class="dot" style="width:8px;height:8px"></i><span class="name">Brightpath Strategic<br>Advisers F.Z.E</span></div>
  <svg class="swoosh" style="bottom:0;height:20px" viewBox="0 0 156 20" preserveAspectRatio="none" aria-hidden="true">
    <path d="M0 6 C50 18 110 16 156 4 V20 H0Z" fill="var(--grey)"/>
    <path d="M0 12 C60 20 110 18 156 12 V20 H0Z" fill="var(--orange)"/>
  </svg>
</div>
<div class="label" style="left:720px;top:226px;">Compliment Slip</div>

<!-- DL envelope -->
<div class="sheet" style="left:840px;top:110px;width:170px;height:112px;">
  <div class="brand" style="left:10px;top:8px;font-size:4px;"><i class="dot" style="width:8px;height:8px"></i><span class="name">Brightpath Strategic<br>Advisers F.Z.E</span></div>
  <svg class="swoosh" style="bottom:0;height:22px" viewBox="0 0 170 22" preserveAspectRatio="none" aria-hidden="true">
    <path d="M0 8 C60 20 120 18 170 4 V22 H0Z" fill="var(--grey)"/>
    <path d="M0 14 C70 22 120 20 170 14 V22 H0Z" fill="var(--orange)"/>
  </svg>
</div>
<div class="label" style="left:905px;top:226px;">DL Envelope</div>

<!-- Envelope colour options -->
<div class="sheet" style="left:1022px;top:44px;width:166px;height:50px;background:linear-gradient(90deg,var(--orange),var(--orange-light));">
  <div class="brand on-dark" style="left:72px;top:16px;font-size:4px;"><i class="dot" style="width:12px;height:12px"></i></div>
</div>
<div class="sheet" style="left:1022px;top:100px;width:166px;height:50px;background:linear-gradient(90deg,var(--grey-dark),var(--grey));">
  <div class="brand" style="left:72px;top:16px;font-size:4px;"><i class="dot" style="width:12px;height:12px"></i></div>
</div>
<div class="sheet" style="left:1022px;top:156px;width:166px;height:66px;">
  <div class="envelope-flap" style="background:#f4f4f4;border-bottom:1px solid #ddd;"></div>
  <div class="brand" style="left:72px;top:14px;font-size:4px;"><i class="dot" style="width:12px;height:12px"></i></div>
</div>
<div class="label" style="left:1075px;top:226px;">Envelope Color Options</div>

</body>
</html>
```